Sports guard Postcard

We are opening a new dental office in Mead, WA and would like to market to the young families that are involved in sports programs.
What we are looking for on a post card are pictures of young athletes playing football, soccer, basketball and hockey and than talk a bit about the importance of sports guard when you are doing sports. Our marketing campaign is to do free sports guards to students who can show that they are signed up with a team. I will send you a copy of our logo so you can see what our colors are.

Here is our address, phone number and web site for the mailing side. Cedar Brook Dental 22856 W. Larkfield Ave. Suite B Brookhaven, WA 99048 509-738-1946 CedarbrookDentist.example

I just realized a error that I made. These sports guard are to be mouth guard for teeth. Hope that was not confusing.

```html
<!DOCTYPE html>
<html lang="en">
<head>
<meta charset="utf-8">
<title>Cedar Brook Dental – Sports Guard Postcard</title>
<link href="https://fonts.googleapis.com/css2?family=Cinzel:wght@400;600&family=Crimson+Text:wght@400;600;700&family=Oswald:wght@500&display=swap" rel="stylesheet">
<style>
  :root{
    --stage:#2b2b2b;
    --plum:#8c1d57;
    --plum-dark:#6e1544;
    --olive:#6b6a2c;
    --paper:#ffffff;
    --ink:#3a3a3a;
    --ink-soft:#555;
  }
  *{box-sizing:border-box;margin:0;padding:0}
  html,body{width:806px;height:1200px;overflow:hidden}
  body{background:var(--stage);position:relative;font-family:"Crimson Text",serif;color:var(--ink)}

  .postcard{position:absolute;left:75px;width:660px;height:513px;background:var(--paper);overflow:hidden}
  .postcard--front{top:47px}
  .postcard--back{top:608px}

  .shapes{position:absolute;inset:0;width:100%;height:100%}

  /* Front */
  .action-photo{position:absolute;left:0;top:0;width:660px;height:360px;
    background:radial-gradient(ellipse at 50% 30%,#9aa3ab 0%,#5f6870 45%,#2f353b 100%)}
  .tagline-banner{position:absolute;left:45px;top:205px;width:240px;height:308px;
    display:flex;flex-direction:column;justify-content:flex-end;align-items:center;padding-bottom:18px;
    font-family:"Cinzel",serif;color:var(--paper);text-align:center;line-height:1.03}
  .tagline-banner span{display:block;font-size:33px;font-weight:600}
  .tagline-banner .tagline-small{font-size:28px}
  .tagline-banner .tagline-big{font-size:46px;margin-top:4px}
  .practice-name{position:absolute;left:400px;top:420px;width:230px;
    font-family:"Cinzel",serif;font-weight:600;color:var(--olive);line-height:1}
  .practice-name .name{display:flex;align-items:center;gap:8px;font-size:24px}
  .practice-name .dot{width:12px;height:12px;border-radius:50%;background:var(--olive);flex:none}
  .practice-name .doctor{display:block;margin-top:6px;margin-left:20px;font-family:"Crimson Text",serif;
    font-size:12px;font-weight:600;color:var(--ink-soft);letter-spacing:.5px}

  /* Back */
  .info-panel{position:absolute;left:0;top:0;width:360px;height:513px}
  .section{position:absolute;left:21px;width:322px}
  .section h2{font-family:"Cinzel",serif;font-weight:600;font-size:22px;letter-spacing:.3px}
  .section p{font-size:13.4px;line-height:1.2;margin-top:6px}
  .section--dentistry{top:14px}
  .section--dentistry h2{color:var(--plum)}
  .section--injury{top:196px;color:var(--paper)}
  .section--injury p{color:#f3e6ed}
  .offer{position:absolute;left:0;top:318px;width:360px;text-align:center;color:var(--paper)}
  .offer h3{font-family:"Oswald",sans-serif;font-weight:500;font-size:28px;line-height:1;letter-spacing:.2px}
  .offer p{font-family:"Crimson Text",serif;font-weight:700;font-size:12.5px;line-height:1.25;letter-spacing:.6px;margin-top:5px}
  .contact{position:absolute;left:22px;top:408px;list-style:none;color:var(--plum-dark);font-size:13px;font-weight:600;line-height:1.2}
  .contact li{display:flex;gap:8px;margin-bottom:8px}
  .contact svg{flex:none;margin-top:2px}
  .stamp-box{position:absolute;left:566px;top:104px;width:61px;height:61px;border:1.5px solid #222}
  .address-line{position:absolute;left:427px;width:216px;height:1.5px;background:#222}
  .address-line--1{top:277px}
  .address-line--2{top:303px}
  .address-line--3{top:331px}
</style>
</head>
<body>

<section class="postcard postcard--front">
  <div class="action-photo" role="img" aria-label="Photo of two young soccer players competing for the ball in the rain on a floodlit field"></div>
  <svg class="shapes" viewBox="0 0 660 513" aria-hidden="true">
    <defs>
      <linearGradient id="mistFade" x1="0" y1="0" x2="0" y2="1">
        <stop offset="0" stop-color="#f4f4f4"/><stop offset="1" stop-color="#d6d6d6"/>
      </linearGradient>
      <linearGradient id="plumFade" x1="0" y1="0" x2="1" y2="0">
        <stop offset="0" stop-color="#7a184b"/><stop offset=".5" stop-color="#9a2563"/><stop offset="1" stop-color="#7a184b"/>
      </linearGradient>
    </defs>
    <path d="M0 330 C180 300 380 300 500 300 C570 300 620 285 660 250 L660 513 L0 513 Z" fill="url(#mistFade)"/>
    <path d="M0 338 C150 318 300 318 420 330 C500 338 540 350 560 388 C460 350 300 345 0 358 Z" fill="var(--olive)"/>
    <path d="M470 330 C560 330 620 300 660 255 L660 340 C620 345 560 345 470 330 Z" fill="url(#plumFade)"/>
    <path d="M45 205 C110 190 180 205 285 188 L285 513 L45 513 Z" fill="url(#plumFade)"/>
  </svg>
  <h1 class="tagline-banner">
    <span>Healthy</span><span>Smiles</span><span class="tagline-small">for a</span><span>Healthy</span><span class="tagline-big">Life</span>
  </h1>
  <div class="practice-name">
    <span class="name"><span class="dot"></span>Cedar Brook Dental</span>
    <span class="doctor">Helen M. Parry, DDS</span>
  </div>
</section>

<section class="postcard postcard--back">
  <svg class="shapes" viewBox="0 0 660 513" aria-hidden="true">
    <defs>
      <linearGradient id="panelFade" x1="0" y1="0" x2="1" y2="0">
        <stop offset="0" stop-color="#ffffff"/><stop offset=".8" stop-color="#f1f1f1"/><stop offset="1" stop-color="#d4d4d4"/>
      </linearGradient>
    </defs>
    <rect x="0" y="0" width="360" height="513" fill="url(#panelFade)"/>
    <path d="M0 196 C90 178 160 152 250 160 C300 164 330 170 360 162 L360 316 L0 316 Z" fill="var(--plum)"/>
    <path d="M0 314 L360 314 L360 418 C300 405 230 386 150 392 C90 396 40 408 0 398 Z" fill="var(--olive)"/>
  </svg>
  <div class="info-panel">
    <div class="section section--dentistry">
      <h2>Sports Dentistry</h2>
      <p>Sports dentistry is the prevention and treatment of dental injuries and related oral diseases, as well as the sharing of information and equipment designed to help protect the teeth, mouth, jaw, and face of athletes of all ages. Injuries to the teeth and mouth are common among athletes. It's important to protect your child's smile if he or she plays sports, for aesthetics as well as health reasons.</p>
    </div>
    <div class="section section--injury">
      <h2>Preventing Injury</h2>
      <p>One of the best ways to prevent injury to your child's teeth and mouth while playing sports is to wear a mouthguard. There are several types of mouthguards to choose from, and your doctor can help you choose the best one for your child's particular needs.</p>
    </div>
    <div class="offer">
      <h3>FREE SPORTS GUARDS</h3>
      <p>TO STUDENTS WHO CAN SHOW THAT<br>THEY ARE SIGNED UP WITH A TEAM</p>
    </div>
    <ul class="contact">
      <li>
        <svg width="9" height="12" viewBox="0 0 9 12"><path d="M4.5 0C2 0 0 2 0 4.4 0 7.6 4.5 12 4.5 12S9 7.6 9 4.4C9 2 7 0 4.5 0Zm0 6.2a1.8 1.8 0 1 1 0-3.6 1.8 1.8 0 0 1 0 3.6Z" fill="var(--plum)"/></svg>
        <span>Cedar Brook Dental<br>22856 W. Larkfield Ave.<br>Suite B Brookhaven, WA 99048</span>
      </li>
      <li>
        <svg width="10" height="10" viewBox="0 0 10 10"><path d="M2 0 3.6 2.6 2.6 3.8C3.3 5.2 4.8 6.7 6.2 7.4L7.4 6.4 10 8 9 9.6C5 10 0 5 .4 1Z" fill="var(--plum)"/></svg>
        <span>509-738-1946</span>
      </li>
      <li>
        <svg width="9" height="9" viewBox="0 0 9 9"><circle cx="4.5" cy="4.5" r="4" fill="var(--plum)"/></svg>
        <span>www.CedarbrookDentist.example</span>
      </li>
    </ul>
  </div>
  <div class="stamp-box"></div>
  <div class="address-line address-line--1"></div>
  <div class="address-line address-line--2"></div>
  <div class="address-line address-line--3"></div>
</section>

</body>
</html>
```